Four Key Ledger Blueprint Presentation

I would like a flyer to hand out to participants at the speeches that we give. We are a CPA firm that specializes in entrepreneurs and realtors. We would like a flyer that looks crisp and clean, that integrates our logo and our company colors (shades of blue & gold). We would like the wording to be as laid out in the attached documents, but design is up to you. We would like a picture to go along with each point and are open to ideas. The flyer should be one page, preferably just the front.

Colors
3176b5
fee18a

Requirements
Must have
• Our logo and the wording supplied.
• A picture to go along with each topic.
Nice to have
• Images that pop, clean look, professional.
Should not have
• Look messy.

```html
<!DOCTYPE html>
<html lang="en">
<head>
<meta charset="utf-8">
<title>Four Key Ledger Blueprint Presentation</title>
<link rel="stylesheet" href="https://fonts.googleapis.com/css2?family=Lato:ital,wght@0,400;0,700;0,900;1,400&family=Lora:ital,wght@1,600&family=Oswald:wght@700&display=swap">
<style>
  :root{
    --navy:#2c4f96;
    --footer:#2f5a9e;
    --gold:#cfa84f;
    --gold-text:#c9a44a;
    --band:#dfc58f;
    --tab:#6b8fc0;
    --ribbon:#efefef;
    --ribbon-shade:#e2e2e2;
    --body:#555a60;
    --backdrop:#e9e9e9;
    --white:#ffffff;
  }
  *{box-sizing:border-box;margin:0;padding:0}
  html,body{width:1200px;height:1200px;overflow:hidden;background:var(--backdrop)}
  .page{position:absolute;left:176px;top:0;width:848px;height:1200px;background:var(--white);font-family:"Lato",sans-serif;color:var(--body)}
  .brand{position:absolute;top:28px;left:0;width:100%;text-align:center}
  .brand-name{font-family:"Lato",sans-serif;font-weight:900;font-size:44px;line-height:48px;color:var(--navy);letter-spacing:.5px}
  .brand-tagline{font-family:"Lora",serif;font-style:italic;font-weight:600;font-size:12px;color:#222;margin-top:18px}
  .title-band{position:absolute;top:135px;left:0;width:100%;height:69px;background:var(--band);display:flex;align-items:center;justify-content:center}
  .title-band h1{font-family:"Oswald",sans-serif;font-weight:700;font-size:38px;color:var(--navy);letter-spacing:-.3px}
  .step{position:absolute;left:0;width:100%;height:112px}
  .ribbon{position:absolute;top:26px;height:62px;background:linear-gradient(to bottom,var(--ribbon) 0%,var(--ribbon) 82%,var(--ribbon-shade) 100%);box-shadow:0 6px 6px -4px rgba(0,0,0,.12)}
  .step.odd .ribbon{left:140px;width:650px}
  .step.even .ribbon{left:55px;width:660px}
  .hex{position:absolute;top:0;width:125px;height:112px}
  .step.odd .hex{left:53px}
  .step.even .hex{left:662px}
  .tab{position:absolute;top:20px;width:60px;height:62px;background:var(--tab);border-radius:6px 6px 6px 20px;color:var(--white);font-family:"Oswald",sans-serif;font-weight:700;font-size:38px;line-height:60px;text-align:center}
  .step.odd .tab{left:733px;border-radius:6px 6px 6px 20px}
  .step.even .tab{left:50px;border-radius:6px 6px 20px 6px}
  .copy{position:absolute;font-size:12.5px;line-height:15.5px;color:var(--body)}
  .copy b{color:#333;font-weight:700}
  .step.odd .copy{left:208px;width:510px;text-align:left}
  .step.even .copy{left:130px;width:503px;text-align:right}
  .slogan{position:absolute;top:910px;left:0;width:100%;text-align:center;font-weight:900;font-size:26px;line-height:31px;letter-spacing:-.3px}
  .slogan .top{color:var(--gold-text)}
  .slogan .bottom{color:var(--navy)}
  .footer{position:absolute;top:1023px;left:0;width:100%;height:177px;background:var(--footer);color:var(--white);text-align:center;padding-top:17px}
  .footer .firm{font-size:21px;line-height:28px}
  .footer .address{font-weight:700;font-size:16px;margin-top:6px}
  .footer .lines{font-size:17px;margin-top:8px;display:flex;justify-content:center;gap:22px;align-items:center}
  .footer .lines span{display:inline-flex;align-items:center;gap:10px}
  .footer .mail{font-size:14px;margin-top:8px}
  .footer .web{font-weight:700;font-size:16px;margin-top:7px}
</style>
</head>
<body>
<div class="page">
  <header class="brand">
    <div class="brand-name">Steadfast Ledger</div>
    <div class="brand-tagline">A Professional Accounting Corporation</div>
  </header>

  <div class="title-band"><h1>Four Key Ledger Blueprint Presentation</h1></div>

  <!-- Step 1 -->
  <section class="step odd" style="top:218px">
    <div class="ribbon"></div>
    <svg class="hex" viewBox="0 0 125 112"><polygon points="31,3 94,3 122,56 94,109 31,109 3,56" fill="var(--gold)" stroke="var(--footer)" stroke-width="6" stroke-linejoin="round"/><circle cx="62.5" cy="56" r="28" fill="#e2c67f" role="img" aria-label="Icon of scissors cutting a dollar bill"/></svg>
    <p class="copy" style="top:34px">We will first show you how to eliminate much of your self-employment tax on your return by converting your business into an S Corporation.&nbsp;&nbsp; A business owner making over <b>$120,000</b> per year can save about <b>$12,000</b> per year by doing this.</p>
    <div class="tab">1</div>
  </section>

  <!-- Step 2 -->
  <section class="step even" style="top:322px">
    <div class="ribbon"></div>
    <div class="tab">2</div>
    <p class="copy" style="top:34px">We will show you how to get tax free income from your corporation by renting you home to the corporation for the board meetings.&nbsp;&nbsp; Many of our clients are getting up to <b>$21,000</b> in tax free income which could put <b>$8,400</b>&nbsp; cash into your pocket.</p>
    <svg class="hex" viewBox="0 0 125 112"><polygon points="31,3 94,3 122,56 94,109 31,109 3,56" fill="var(--gold)" stroke="var(--footer)" stroke-width="6" stroke-linejoin="round"/><circle cx="62.5" cy="56" r="26" fill="none" stroke="#fff" stroke-width="5"/><text x="62.5" y="63" text-anchor="middle" font-family="Oswald,sans-serif" font-weight="700" font-size="20" fill="#fff">TAX</text><line x1="44" y1="38" x2="81" y2="74" stroke="#fff" stroke-width="5"/></svg>
  </section>

  <!-- Step 3 -->
  <section class="step odd" style="top:416px">
    <div class="ribbon"></div>
    <svg class="hex" viewBox="0 0 125 112"><polygon points="31,3 94,3 122,56 94,109 31,109 3,56" fill="var(--gold)" stroke="var(--footer)" stroke-width="6" stroke-linejoin="round"/><rect x="36" y="33" width="53" height="36" rx="3" fill="none" stroke="#fff" stroke-width="4"/><rect x="55" y="69" width="15" height="6" fill="#fff"/><rect x="48" y="75" width="29" height="4" fill="#fff"/><rect x="44" y="52" width="4" height="11" fill="#fff"/><rect x="50" y="46" width="4" height="17" fill="#fff"/><rect x="56" y="55" width="4" height="8" fill="#fff"/><circle cx="73" cy="51" r="9" fill="#fff"/><path d="M73 51 L73 42 A9 9 0 0 1 82 51 Z" fill="var(--gold)"/></svg>
    <p class="copy" style="top:34px">We will show you the easiest way to track your expenses so that the only thing you will have to do to have rock solid books is to take a picture of the receipt and throw it away. It doesn’t get any better than that.</p>
    <div class="tab">3</div>
  </section>

  <!-- Step 4 -->
  <section class="step even" style="top:519px">
    <div class="ribbon"></div>
    <div class="tab">4</div>
    <p class="copy" style="top:41px">Next, we show you the importance of tax planning and why it is critical to meet with your CPA before the end of the year and not just when you do your tax preparation.</p>
    <svg class="hex" viewBox="0 0 125 112"><polygon points="31,3 94,3 122,56 94,109 31,109 3,56" fill="var(--gold)" stroke="var(--footer)" stroke-width="6" stroke-linejoin="round"/><rect x="40" y="30" width="40" height="54" rx="3" fill="none" stroke="#fff" stroke-width="4"/><rect x="52" y="25" width="16" height="8" rx="2" fill="#fff"/><g fill="#fff"><rect x="46" y="42" width="4" height="4"/><rect x="53" y="42" width="18" height="3"/><rect x="46" y="52" width="4" height="4"/><rect x="53" y="52" width="14" height="3"/><rect x="46" y="62" width="4" height="4"/><rect x="53" y="62" width="10" height="3"/><rect x="46" y="72" width="4" height="4"/><rect x="53" y="72" width="10" height="3"/></g><circle cx="80" cy="65" r="13" fill="#fff"/><path d="M73 65 L78 70 L87 60" fill="none" stroke="var(--gold)" stroke-width="3"/></svg>
  </section>

  <!-- Step 5 -->
  <section class="step odd" style="top:621px">
    <div class="ribbon"></div>
    <svg class="hex" viewBox="0 0 125 112"><polygon points="31,3 94,3 122,56 94,109 31,109 3,56" fill="var(--gold)" stroke="var(--footer)" stroke-width="6" stroke-linejoin="round"/><rect x="50" y="22" width="25" height="68" rx="12" fill="#e2c67f" role="img" aria-label="Icon of a standing child"/></svg>
    <p class="copy" style="top:41px">We will show you how to hire your children and get <b>$7,500</b> per child tax free.&nbsp;&nbsp; This will save you <b>$3,000</b> per child in income tax reduction.</p>
    <div class="tab">5</div>
  </section>

  <!-- Step 6 -->
  <section class="step even" style="top:720px">
    <div class="ribbon"></div>
    <div class="tab">6</div>
    <p class="copy" style="top:33px">We will discuss how to make your child’s college education tax deductible.&nbsp;&nbsp; With college cost spiraling out of control this is a biggie.&nbsp;&nbsp; Most of our clients have a savings of about <b>$12,000</b> per year of college.</p>
    <svg class="hex" viewBox="0 0 125 112"><polygon points="31,3 94,3 122,56 94,109 31,109 3,56" fill="var(--gold)" stroke="var(--footer)" stroke-width="6" stroke-linejoin="round"/><rect x="34" y="36" width="57" height="40" rx="6" fill="#e2c67f" role="img" aria-label="Icon of a graduation cap"/></svg>
  </section>

  <!-- Step 7 -->
  <section class="step odd" style="top:819px">
    <div class="ribbon"></div>
    <svg class="hex" viewBox="0 0 125 112"><polygon points="31,3 94,3 122,56 94,109 31,109 3,56" fill="var(--gold)" stroke="var(--footer)" stroke-width="6" stroke-linejoin="round"/><text x="28" y="78" font-family="Lato,sans-serif" font-size="56" fill="#fff">0</text><text x="66" y="78" font-family="Lato,sans-serif" font-size="26" fill="#fff">%</text></svg>
    <p class="copy" style="top:34px;left:215px">Our grand finale is to show you how to use, not one, but two corporations to get a several hundred thousand dollar tax deferral, get an interest free loan from the government and use that money to grow your business and your wealth.</p>
    <div class="tab">7</div>
  </section>

  <div class="slogan">
    <div class="top">IF THEY DRIVE BY WITH A MACHINE GUN</div>
    <div class="bottom">YOU DON’T HAVE TO STAND UP</div>
  </div>

  <footer class="footer">
    <div class="firm">Steadfast Ledger, A Professional Accounting Corporation</div>
    <div class="address">2718 N. Elm Ave, Ste. B, Lodi, CA 95240</div>
    <div class="lines">
      <span><svg width="20" height="20" viewBox="0 0 24 24"><path d="M6.6 10.8a15.1 15.1 0 0 0 6.6 6.6l2.2-2.2a1 1 0 0 1 1-.25 11.4 11.4 0 0 0 3.6.57 1 1 0 0 1 1 1V20a1 1 0 0 1-1 1A17 17 0 0 1 3 4a1 1 0 0 1 1-1h3.5a1 1 0 0 1 1 1c0 1.25.2 2.45.57 3.57a1 1 0 0 1-.25 1z" fill="#fff"/></svg>555-014-2231</span>
      <span><svg width="24" height="20" viewBox="0 0 24 20"><rect x="6" y="0" width="12" height="6" fill="#fff"/><rect x="1" y="7" width="22" height="9" rx="2" fill="#fff"/><rect x="6" y="12" width="12" height="8" fill="#fff" stroke="var(--footer)" stroke-width="1.5"/></svg>555-014-2290</span>
    </div>
    <div class="mail">ellen@steadfastledgercpas.com /marcus@steadfastledgercpas.com</div>
    <div class="web">www.steadfastledgercpa.com</div>
  </footer>
</div>
</body>
</html>
```